Business Card Design

We need a business card design that can also be aplied for postcards. We are a small indie record company that also do consulting, and development of independat artitst . I already have the name and the basic idea of what i am looking for but i am open to any suggestion.
Info for the card
Name of the company : Velmora Records
NAME : Tobias Lindqvist
PHONE : 314-5820641
EMAIL : hello@velmorarecords.example
WEB: www.velmorarecords.example
Target Market(s)
Male - Female independent musicians ages 18 to 45
Industry/Entity Type
Record Company
Contact Information for Business Card
Independant records company that also works in consulting for music business models for independent artists
Look and feel

```html
<!DOCTYPE html>
<html lang="en">
<head>
<meta charset="utf-8">
<title>Velmora Records – Business Card</title>
<link rel="stylesheet" href="https://fonts.googleapis.com/css2?family=Ubuntu:wght@400;500&display=swap">
<style>
  :root {
    --page: #e9eaec;
    --card: #ffffff;
    --sky: #a9d0f0;
    --mist: #cfeaf3;
    --brand-blue: #386a96;
    --ink: #1c1c1c;
    --shadow: rgba(0, 0, 0, 0.18);
  }
  * { box-sizing: border-box; margin: 0; padding: 0; }
  html, body {
    width: 1200px;
    height: 926px;
    overflow: hidden;
    background: var(--page);
    font-family: "Ubuntu", Arial, sans-serif;
  }
  .sheet {
    position: relative;
    width: 1200px;
    height: 926px;
  }
  .card {
    position: absolute;
    left: 250px;
    width: 700px;
    height: 400px;
    background: var(--card);
    box-shadow: 0 6px 18px var(--shadow);
    overflow: hidden;
  }
  .card--front { top: 45px; }
  .card--back { top: 481px; }

  .card__backdrop {
    position: absolute;
    inset: 0;
    width: 700px;
    height: 400px;
  }
  .brand {
    position: absolute;
    display: flex;
    align-items: center;
    gap: 14px;
  }
  .brand__dot {
    width: 84px;
    height: 84px;
    border-radius: 50%;
    background: var(--sky);
    border: 5px solid var(--card);
    flex-shrink: 0;
  }
  .brand__name {
    font-size: 27px;
    font-weight: 500;
    letter-spacing: 0.5px;
    color: var(--brand-blue);
    white-space: nowrap;
  }
  .card--front .brand { left: 123px; top: 43px; }

  .person {
    position: absolute;
    left: 205px;
    top: 250px;
    font-size: 21px;
    font-weight: 500;
    color: var(--brand-blue);
  }
  .contacts {
    position: absolute;
    left: 368px;
    top: 282px;
    list-style: none;
  }
  .contacts__item {
    display: flex;
    align-items: center;
    gap: 8px;
    font-size: 18px;
    line-height: 28px;
    color: var(--ink);
  }
  .contacts__icon {
    width: 15px;
    height: 15px;
    fill: var(--brand-blue);
    flex-shrink: 0;
  }

  .card--back .brand {
    left: 0;
    right: 0;
    top: 120px;
    flex-direction: column;
    gap: 16px;
  }
  .card--back .brand__dot {
    width: 78px;
    height: 78px;
  }
</style>
</head>
<body>
<main class="sheet">

  <section class="card card--front" aria-label="Business card front">
    <svg class="card__backdrop" viewBox="0 0 700 400" aria-hidden="true">
      <path d="M0 0 H150 C70 90 45 250 120 400 H0 Z" fill="var(--sky)"/>
      <path d="M150 0 H200 C150 130 190 300 300 400 H120 C45 250 70 90 150 0 Z" fill="var(--mist)"/>
      <path d="M150 0 C70 90 45 250 120 400" fill="none" stroke="var(--card)" stroke-width="5"/>
    </svg>

    <div class="brand">
      <span class="brand__dot"></span>
      <span class="brand__name">VELMORA RECORDS</span>
    </div>

    <p class="person">Tobias Lindqvist</p>

    <ul class="contacts">
      <li class="contacts__item">
        <svg class="contacts__icon" viewBox="0 0 16 16" aria-hidden="true">
          <path d="M2 6 C2 3 5 2 8 2 C11 2 14 3 14 6 L11 7 L10 5 H6 L5 7 Z"/>
          <path d="M4 8 H12 L13 14 H3 Z"/>
        </svg>
        <span>314-5820641</span>
      </li>
      <li class="contacts__item">
        <svg class="contacts__icon" viewBox="0 0 16 16" aria-hidden="true">
          <rect x="1" y="3" width="14" height="10"/>
          <path d="M1 3 L8 9 L15 3" fill="none" stroke="#fff" stroke-width="1.3"/>
        </svg>
        <span>hello@velmorarecords.example</span>
      </li>
      <li class="contacts__item">
        <svg class="contacts__icon" viewBox="0 0 16 16" aria-hidden="true">
          <path d="M1 2 H15 V11 H1 Z M2.5 3.5 V9.5 H13.5 V3.5 Z"/>
          <rect x="6" y="11" width="4" height="2"/>
          <rect x="4" y="13" width="8" height="1.5"/>
        </svg>
        <span>www.velmorarecords.example</span>
      </li>
    </ul>
  </section>

  <section class="card card--back" aria-label="Business card back">
    <div class="brand">
      <span class="brand__dot"></span>
      <span class="brand__name">VELMORA RECORDS</span>
    </div>
  </section>

</main>
</body>
</html>
```